Consultant ot credit unions that operate a property and casualty insurance agency

Industry/Entity Type

Insurance

Contact Information for Business Card

Dorian Velcote
Harlow Point Insurance Agency Consultant
dorianvelcote@mailbrook.example
562 318-4092
418 Tamsin Court
Long Beach, CA 90814

```html
<!DOCTYPE html>
<html lang="en">
<head>
<meta charset="utf-8">
<title>Harlow Point Insurance – Business Card</title>
<link rel="stylesheet" href="https://fonts.googleapis.com/css2?family=Arimo:wght@400;700&display=swap">
<style>
  :root {
    --page-bg: #e9e6e1;
    --card-top: #0b4a78;
    --card-bottom: #135a89;
    --ink: #ffffff;
    --card-shadow: rgba(20, 30, 40, 0.25);
  }
  * { margin: 0; padding: 0; box-sizing: border-box; }
  html, body {
    width: 1200px;
    height: 800px;
    overflow: hidden;
    background: var(--page-bg);
  }
  .stage {
    width: 1200px;
    height: 800px;
    display: flex;
    align-items: center;
    justify-content: center;
  }
  .business-card {
    position: relative;
    width: 1050px;
    height: 600px;
    background: linear-gradient(180deg, var(--card-top), var(--card-bottom));
    box-shadow: 0 10px 30px var(--card-shadow);
    color: var(--ink);
    font-family: "Arimo", Arial, sans-serif;
    text-align: center;
  }
  .card-frame {
    position: absolute;
    inset: 0;
  }
  .card-frame path {
    fill: none;
    stroke: var(--ink);
    stroke-width: 2;
  }
  .card-content {
    position: absolute;
    inset: 0;
    display: flex;
    flex-direction: column;
    align-items: center;
  }
  .company-name {
    margin-top: 112px;
    font-size: 84px;
    font-weight: 400;
    letter-spacing: 1px;
    white-space: nowrap;
  }
  .person-name {
    margin-top: 40px;
    font-size: 34px;
    font-weight: 700;
    line-height: 1;
  }
  .person-role {
    margin-top: 2px;
    font-size: 26px;
    font-weight: 400;
    line-height: 1.1;
  }
  .contact-line {
    font-size: 25px;
    font-weight: 400;
    line-height: 1.2;
  }
  .contact-line.phone { margin-top: 44px; }
  .address {
    margin-top: 46px;
    font-size: 34px;
    font-weight: 700;
    white-space: nowrap;
  }
</style>
</head>
<body>
<main class="stage">
  <article class="business-card">
    <svg class="card-frame" viewBox="0 0 1050 600" width="1050" height="600" aria-hidden="true">
      <path d="M58 28 H992 A30 30 0 0 0 1022 58 V542 A30 30 0 0 0 992 572 H58 A30 30 0 0 0 28 542 V58 A30 30 0 0 0 58 28 Z"/>
      <path d="M66 36 H984 A30 30 0 0 0 1014 66 V534 A30 30 0 0 0 984 564 H66 A30 30 0 0 0 36 534 V66 A30 30 0 0 0 66 36 Z"/>
    </svg>
    <div class="card-content">
      <h1 class="company-name">Harlow Point Insurance</h1>
      <p class="person-name">Dorian Velcote</p>
      <p class="person-role">Agency Consultant</p>
      <p class="contact-line phone">562 318-4092</p>
      <p class="contact-line email">dorianvelcote@mailbrook.example</p>
      <p class="address">418 Tamsin Court Long Beach, CA 90814</p>
    </div>
  </article>
</main>
</body>
</html>
```